Business card Zottelgarten

Business card is for a self-employed dog trainer with own dog school. Name and logo of the dog school are available. Color specifications as well. The design should be classy and minimalist, but also modern. An already existing idea would be: Front: Only the logo Back: Contact data

Font styles to use
Serif
Sans Serif
Other font styles liked:
• Trajan Pro

Colors
f78f20

Requirements
Must have
• Name: Margit Wendler-Rasch Title: Dipl. Dog Trainer Contain my logo Follow my font and color preferences (see files)

```html
<!DOCTYPE html>
<html lang="de">
<head>
<meta charset="utf-8">
<title>Zottelgarten – Business Card</title>
<link rel="stylesheet" href="https://fonts.googleapis.com/css2?family=Cinzel:wght@400;700&family=EB+Garamond:wght@400;500&display=swap">
<style>
  :root {
    --canvas: #efebe6;
    --card-orange: #f78f20;
    --ink: #1d1a17;
    --ink-soft: #3a2c20;
    --ghost: rgba(255, 255, 255, 0.14);
    --ghost-text: rgba(120, 60, 10, 0.14);
  }
  * { margin: 0; padding: 0; box-sizing: border-box; }
  html, body {
    width: 1200px; height: 900px; overflow: hidden;
    background: var(--canvas);
  }
  .stage {
    width: 1200px; height: 900px;
    display: flex; align-items: center; justify-content: center; gap: 60px;
  }
  .card {
    position: relative;
    width: 500px; height: 324px;
    background: var(--card-orange);
    box-shadow: 0 10px 24px rgba(0, 0, 0, 0.18);
    overflow: hidden;
    color: var(--ink);
  }

  /* Front */
  .card--front {
    display: flex; align-items: center; justify-content: center; gap: 18px;
  }
  .brand-dot {
    width: 112px; height: 112px; border-radius: 50%;
    background: var(--ink);
    flex-shrink: 0;
  }
  .brand-text { display: flex; flex-direction: column; }
  .brand-name {
    font-family: "Cinzel", serif; font-weight: 400;
    font-size: 34px; letter-spacing: 1px; line-height: 1;
  }
  .brand-url {
    font-family: "Cinzel", serif; font-weight: 400;
    font-size: 9.5px; letter-spacing: 5.2px; margin-top: 6px;
  }

  /* Back */
  .ghost-circle {
    position: absolute; left: 150px; top: 48px;
    width: 180px; height: 180px; border-radius: 50%;
    background: var(--ghost);
  }
  .ghost-name {
    position: absolute; right: 40px; bottom: 60px;
    font-family: "Cinzel", serif; font-weight: 400;
    font-size: 38px; letter-spacing: 2px; line-height: 1;
    color: var(--ghost-text);
    white-space: nowrap;
  }
  .contact {
    position: absolute; left: 76px; top: 96px;
  }
  .person-name {
    font-family: "Cinzel", serif; font-weight: 700;
    font-size: 24px; letter-spacing: 0.5px; line-height: 1;
    white-space: nowrap;
  }
  .person-title {
    font-family: "Cinzel", serif; font-weight: 400;
    font-size: 16px; letter-spacing: 1px; margin-top: 9px;
    color: var(--ink-soft);
  }
  .contact-lines {
    list-style: none; margin-top: 8px;
    font-family: "EB Garamond", serif; font-size: 12px; line-height: 1.45;
    color: var(--ink-soft);
  }
  .web {
    position: absolute; right: 40px; bottom: 26px;
    font-family: "EB Garamond", serif; font-weight: 500; font-size: 15px;
  }
</style>
</head>
<body>
<main class="stage">
  <section class="card card--front" aria-label="Card front">
    <span class="brand-dot" aria-hidden="true"></span>
    <div class="brand-text">
      <span class="brand-name">ZOTTELGARTEN</span>
      <span class="brand-url">WWW.ZOTTELGARTEN.CH</span>
    </div>
  </section>

  <section class="card card--back" aria-label="Card back">
    <span class="ghost-circle" aria-hidden="true"></span>
    <span class="ghost-name" aria-hidden="true">ZOTTELGARTEN</span>
    <div class="contact">
      <h1 class="person-name">MARGIT WENDLER-RASCH</h1>
      <p class="person-title">Dipl. Dog Trainer</p>
      <ul class="contact-lines">
        <li>Contact: 0571 204318</li>
        <li>E-mail: margit@zottelgarten.com</li>
      </ul>
    </div>
    <p class="web">www.zottelgarten.ch</p>
  </section>
</main>
</body>
</html>
```